Maple Hollow Bloom Backdrops Business card

Looking to have a business card design incorporating my logo for my flower wall business.

Industry/Entity Type

Wedding & event planning

Contact Information for Business Card

My business logo, my name - Jill Worthing (owner), my tagline - Let us be your something extra, phone # 401-627-3918, email address - maplehollowbloombackdrops@fernpost.com, my website - maplehollowbloombackdrops.com, Instagram handle- @maplehollowbloombackdrops, FB handle Handle - maplehollowbloombackdrops

Font styles to use
Other font styles liked:
• Sentaina is the font that is used in my logo

Requirements
Must have
• Would like a double sided business card

```html
<!DOCTYPE html>
<html lang="en">
<head>
<meta charset="utf-8">
<title>Maple Hollow Bloom Backdrops – Business Card</title>
<link rel="stylesheet" href="https://fonts.googleapis.com/css2?family=Poppins:wght@300;400&family=Mrs+Saint+Delafield&display=swap">
<style>
  :root {
    --canvas-bg: #2a2a2c;
    --card-white: #ffffff;
    --card-pink: #f9dde9;
    --pattern-pink: #f4cfe0;
    --ink: #1e1e1e;
    --icon-tile: #2b2b2b;
    --icon-pink: #e58fc0;
    --gold: #d9b54a;
    --rule: #3a3a3a;
  }
  html, body {
    margin: 0;
    padding: 0;
    width: 1200px;
    height: 1108px;
    overflow: hidden;
    background: var(--canvas-bg);
  }
  .canvas {
    position: relative;
    width: 1200px;
    height: 1108px;
  }
  .card {
    position: absolute;
    top: 164px;
    width: 440px;
    height: 780px;
    border-radius: 26px;
    box-sizing: border-box;
    overflow: hidden;
  }
  .card--front {
    left: 110px;
    background: var(--card-white);
    text-align: center;
    color: var(--ink);
    font-family: "Poppins", sans-serif;
  }
  .card--back {
    left: 650px;
    background: var(--card-pink);
  }

  /* Front: brand block */
  .brand {
    position: absolute;
    top: 70px;
    left: 0;
    right: 0;
  }
  .brand__mark {
    display: block;
    margin: 0 auto 22px;
  }
  .brand__name {
    margin: 0;
    font-weight: 300;
    font-size: 27px;
    line-height: 1.3;
    letter-spacing: 2px;
    text-transform: uppercase;
    color: var(--ink);
  }

  /* Front: person */
  .person {
    position: absolute;
    top: 330px;
    left: 0;
    right: 0;
  }
  .person__name {
    margin: 0;
    font-family: "Mrs Saint Delafield", cursive;
    font-weight: 400;
    font-size: 64px;
    line-height: 1;
  }
  .person__role {
    margin: 2px 0 0;
    font-weight: 300;
    font-size: 20px;
  }

  /* Front: contact groups */
  .divider {
    display: flex;
    align-items: center;
    justify-content: center;
    gap: 8px;
  }
  .divider__rule {
    width: 52px;
    height: 1px;
    background: var(--rule);
  }
  .icon-tile {
    width: 34px;
    height: 34px;
    border-radius: 5px;
    background: var(--icon-tile);
    display: flex;
    align-items: center;
    justify-content: center;
  }
  .contact {
    position: absolute;
    top: 470px;
    left: 0;
    right: 0;
  }
  .contact__list,
  .social__list {
    list-style: none;
    margin: 12px 0 0;
    padding: 0;
    font-weight: 400;
    font-size: 16.5px;
    line-height: 1.45;
  }
  .social {
    position: absolute;
    top: 625px;
    left: 0;
    right: 0;
  }

  /* Back */
  .back__pattern {
    position: absolute;
    inset: 0;
    background: radial-gradient(circle at 50% 45%, var(--pattern-pink) 0%, var(--card-pink) 75%);
  }
  .back__brand {
    position: absolute;
    right: 44px;
    top: 520px;
    display: flex;
    align-items: center;
    gap: 10px;
    font-family: "Poppins", sans-serif;
    font-weight: 300;
    font-size: 13px;
    letter-spacing: 1.5px;
    text-transform: uppercase;
    color: var(--ink);
  }
  .back__tagline {
    position: absolute;
    left: 0;
    right: 0;
    top: 610px;
    margin: 0;
    text-align: center;
    font-family: "Mrs Saint Delafield", cursive;
    font-weight: 400;
    font-size: 50px;
    color: var(--ink);
  }
</style>
</head>
<body>
<main class="canvas">

  <section class="card card--front" aria-label="Business card front">
    <header class="brand">
      <svg class="brand__mark" width="70" height="70" viewBox="0 0 70 70" aria-hidden="true">
        <circle cx="35" cy="35" r="33" fill="none" stroke="var(--gold)" stroke-width="2"/>
      </svg>
      <h1 class="brand__name">Maple Hollow<br>Bloom Backdrops</h1>
    </header>

    <div class="person">
      <p class="person__name">Jill Worthing</p>
      <p class="person__role">Owner</p>
    </div>

    <div class="contact">
      <div class="divider">
        <span class="divider__rule"></span>
        <span class="icon-tile" aria-label="Phone">
          <svg width="20" height="20" viewBox="0 0 24 24"><path fill="var(--icon-pink)" d="M6.6 10.8a15 15 0 0 0 6.6 6.6l2.2-2.2a1 1 0 0 1 1-.25 11.4 11.4 0 0 0 3.6.6 1 1 0 0 1 1 1V20a1 1 0 0 1-1 1A17 17 0 0 1 3 4a1 1 0 0 1 1-1h3.5a1 1 0 0 1 1 1c0 1.25.2 2.45.6 3.6a1 1 0 0 1-.25 1z"/></svg>
        </span>
        <span class="icon-tile" aria-label="Email">
          <svg width="20" height="20" viewBox="0 0 24 24"><rect x="2" y="5" width="20" height="14" rx="1.5" fill="var(--icon-pink)"/><path d="M2.5 6l9.5 7 9.5-7" fill="none" stroke="var(--icon-tile)" stroke-width="1.6"/></svg>
        </span>
        <span class="icon-tile" aria-label="Website">
          <svg width="20" height="20" viewBox="0 0 24 24"><circle cx="12" cy="12" r="9.5" fill="var(--icon-pink)"/><path d="M2.5 12h19M12 2.5c3 3 3 16 0 19M12 2.5c-3 3-3 16 0 19" fill="none" stroke="var(--icon-tile)" stroke-width="1.3"/></svg>
        </span>
        <span class="divider__rule"></span>
      </div>
      <ul class="contact__list">
        <li>401-627-3918</li>
        <li>maplehollowbloombackdrops@fernpost.com</li>
        <li>maplehollowbloombackdrops.com</li>
      </ul>
    </div>

    <div class="social">
      <div class="divider">
        <span class="divider__rule"></span>
        <span class="icon-tile" aria-label="Social profile"></span>
        <span class="icon-tile" aria-label="Social page"></span>
        <span class="divider__rule"></span>
      </div>
      <ul class="social__list">
        <li>@maplehollowbloombackdrops</li>
        <li>maplehollowbloombackdrops</li>
      </ul>
    </div>
  </section>

  <section class="card card--back" aria-label="Business card back">
    <div class="back__pattern" role="img" aria-label="Faint repeating pink floral emblem pattern"></div>
    <div class="back__brand">
      <svg width="40" height="40" viewBox="0 0 40 40" aria-hidden="true">
        <circle cx="20" cy="20" r="18.5" fill="none" stroke="var(--gold)" stroke-width="1.6"/>
      </svg>
      <span>Maple Hollow Bloom Backdrops</span>
    </div>
    <p class="back__tagline">Let us be your something extra</p>
  </section>

</main>
</body>
</html>
```